Mailchimp email (Monthly performance report design)

We need someone to code an HTML file as this will be used to import the template to Mailchimp.

We need a slick and professionally designed email layout to be used via Mailchimp. The target audience is sophisticated investors.

We have attached our current email template that is being used (File name: Capture 1). We have also added an inspiration piece (File name: Capture). The content needs to be transferred to the new template. We have 3 funds and we want them to be somehow presented in 3 columns. The pictures need to be professional business or nature bleu theme. We have also uploaded a template to provide you with guidance on how the layout should be. You are free to use your imagination and make changes as deemed.

This is our website: https://www.tarnwellholdings.com/. The color theme of the template should match the website.

The pictures need to be professional business or nature bleu theme.

Coding

```html
<!DOCTYPE html>
<html lang="en">
<head>
<meta charset="utf-8">
<title>Tarnwell Monthly Report</title>
<link href="https://fonts.googleapis.com/css2?family=Arimo:wght@400;600;700&family=Heebo:wght@400;500&display=swap" rel="stylesheet">
<style>
:root{
  --navy:#1f3450;
  --ink:#1c1c1c;
  --panel:#282828;
  --white:#ffffff;
  --mist:#eef0f3;
  --text:#2a2a2a;
}
*{margin:0;padding:0;box-sizing:border-box}
html,body{width:1200px;height:2499px;overflow:hidden;background:var(--white)}
body{font-family:"Heebo",sans-serif;color:var(--text);position:relative}
.header{position:absolute;left:0;top:0;width:1200px;height:130px}
.brand{position:absolute;display:flex;align-items:center;gap:16px;font-family:"Arimo",sans-serif;font-weight:600;color:var(--ink);letter-spacing:3px}
.brand-mark{border-radius:50%;background:var(--ink)}
.header .brand{left:92px;top:30px;font-size:30px}
.header .brand-mark{width:70px;height:70px}
.nav{position:absolute;top:55px;left:798px;display:flex;gap:0;font-size:23px;color:var(--ink)}
.nav a{color:inherit;text-decoration:none;margin-right:48px}
.hero{position:absolute;top:130px;left:0;width:1200px;height:750px}
.hero-photo-left{position:absolute;left:0;top:0;width:570px;height:750px;background:linear-gradient(160deg,#5b6f88 0%,#2f3d52 55%,#1c2738 100%)}
.hero-panel{position:absolute;left:570px;top:0;width:452px;height:750px;background:var(--panel);color:var(--white);padding:152px 0 0 52px}
.hero-photo-right{position:absolute;left:1022px;top:0;width:178px;height:750px;background:linear-gradient(180deg,#5c6b80,#34435a 60%,#29374b)}
.hero-title{font-family:"Arimo",sans-serif;font-weight:700;font-size:38px;line-height:1}
.hero-rule{width:56px;height:4px;background:var(--white);margin:26px 0 32px}
.hero-copy{font-size:19px;line-height:33px;width:380px}
.funds{position:absolute;top:880px;left:0;width:1200px;height:542px}
.fund{position:absolute;top:110px;width:360px;text-align:center}
.fund svg{display:block;margin:0 auto;height:116px}
.fund-name{font-family:"Arimo",sans-serif;font-weight:600;font-size:25px;color:var(--ink);margin-top:40px}
.fund-copy{font-size:15px;line-height:31.5px;margin-top:24px;color:var(--ink)}
.purpose{position:absolute;top:1422px;left:0;width:1200px;height:598px;background:linear-gradient(90deg,#e9ebef,#f1f2f4 50%,#e7e9ed)}
.portrait{position:absolute;left:90px;top:111px;width:367px;height:378px;border-radius:12px;background:linear-gradient(150deg,#d6dbe1 0%,#8f8a84 55%,#4d4a47 100%)}
.purpose-text{position:absolute;left:539px;top:85px;width:571px}
.purpose h2{font-family:"Arimo",sans-serif;font-weight:600;font-size:29px;color:var(--ink)}
.purpose p{font-size:19.5px;line-height:34.5px;text-align:justify;margin-top:18px;color:#333}
.purpose h2.second{margin-top:26px}
.purpose p.note{margin-top:0;text-align:left}
.footer{position:absolute;top:2020px;left:0;width:1200px;height:414px}
.footer .brand{left:95px;top:110px;font-size:40px;letter-spacing:5px}
.footer .brand-mark{width:108px;height:108px}
.address{position:absolute;left:705px;top:82px}
.address h3{font-family:"Arimo",sans-serif;font-weight:600;font-size:32px;color:var(--ink);margin-bottom:32px}
.contact-row{display:flex;gap:26px;font-size:21px;line-height:33px;color:var(--ink);margin-bottom:13px}
.contact-row svg{width:22px;height:22px;margin-top:6px;flex:none}
.bar{position:absolute;top:2434px;left:0;width:1200px;height:65px;background:var(--navy);color:var(--white);font-size:20px;display:flex;align-items:center;justify-content:center}
.bar .sep{margin:0 16px}
.social{position:absolute;right:84px;top:24px;width:22px;height:22px;background:var(--white);border-radius:3px}
</style>
</head>
<body>
<header class="header">
  <div class="brand"><span class="brand-mark"></span>TARNWELL</div>
  <nav class="nav"><a href="#">About</a><a href="#">Fund</a><a href="#">Contact</a></nav>
</header>

<section class="hero">
  <div class="hero-photo-left" role="img" aria-label="Business team meeting around a table in a glass-walled office"></div>
  <div class="hero-panel">
    <h1 class="hero-title">Monthly Report</h1>
    <div class="hero-rule"></div>
    <p class="hero-copy">Tarnwell is a specialist fundamental investor focused on smaller-capitalization equities. Our clients benefit from a fully committed team with deep expertise in a market segment with numerous inefficiencies. We manage capital for sophisticated clientele of institutional investors, foundations &amp; endowments, family offices, funds of funds and select investment advisors.</p>
  </div>
  <div class="hero-photo-right" role="img" aria-label="Glass office facade with city reflections"></div>
</section>

<section class="funds">
  <div class="fund" style="left:47px">
    <svg viewBox="0 0 90 116" fill="none" stroke="#1f3450" stroke-width="4" stroke-linecap="round">
      <path d="M45 20a25 25 0 0 0-15 45c4 3 5 7 5 12h20c0-5 1-9 5-12a25 25 0 0 0-15-45z"/>
      <path d="M36 85h18M36 93h18M40 101h10"/>
      <path d="M45 2v6M18 12l4 4M72 12l-4 4M5 40h6M79 40h6"/>
      <text x="45" y="54" text-anchor="middle" font-family="Arimo,sans-serif" font-size="26" font-weight="700" fill="#1f3450" stroke="none">$</text>
    </svg>
    <div class="fund-name">Opportunities Fund</div>
    <p class="fund-copy">Lorem ipsum dolor sit amet,<br>consectetur adipiscing elit, sed do<br>eiusmod tempor incididunt</p>
  </div>
  <div class="fund" style="left:423px">
    <svg viewBox="0 0 120 116" fill="none" stroke="#1f3450" stroke-width="4" stroke-linecap="round" stroke-linejoin="round">
      <circle cx="78" cy="30" r="26"/>
      <text x="78" y="41" text-anchor="middle" font-family="Arimo,sans-serif" font-size="30" font-weight="700" fill="#1f3450" stroke="none">$</text>
      <path d="M6 80h20v30H6zM26 84h24c6 0 8 8 0 8H38M50 92l40-14c12-4 14 4 6 8L60 104H26"/>
    </svg>
    <div class="fund-name">Canadian Small Cap Fund</div>
    <p class="fund-copy">Lorem ipsum dolor sit amet,<br>consectetur adipiscing elit, sed do<br>eiusmod tempor incididunt</p>
  </div>
  <div class="fund" style="left:800px">
    <svg viewBox="0 0 110 116" fill="none" stroke="#1f3450" stroke-width="4" stroke-linejoin="round">
      <path d="M25 4h60v30H62l-7 8-7-8H25z"/>
      <text x="55" y="27" text-anchor="middle" font-family="Arimo,sans-serif" font-size="18" font-weight="700" fill="#1f3450" stroke="none">FUND</text>
      <path d="M6 72h26v8H6zM6 84h26v8H6zM6 96h26v8H6zM42 60h26v8H42zM42 72h26v8H42zM42 84h26v8H42zM42 96h26v8H42zM78 72h26v8H78zM78 84h26v8H78zM78 96h26v8H78z"/>
    </svg>
    <div class="fund-name">U.S. Small Cap Fund</div>
    <p class="fund-copy">Lorem ipsum dolor sit amet,<br>consectetur adipiscing elit, sed do<br>eiusmod tempor incididunt</p>
  </div>
</section>

<section class="purpose" role="img" aria-label="Faded background of colleagues in a meeting">
  <div class="portrait" role="img" aria-label="Portrait of a smiling businessman in a bright office"></div>
  <div class="purpose-text">
    <h2>Our Raison d'être</h2>
    <p>High-quality smaller-capitalization companies are often materially mispriced relative to fundamentals. Our specialized investment team can take advantage of these inefficiencies to deliver industry-leading returns to our clients.</p>
    <h2 class="second">Our Mission</h2>
    <p>Our mission is to provide the highest possible value to our clients while making a positive impact on society.</p>
    <p class="note">The logo at the botton need to centralized</p>
  </div>
</section>

<footer class="footer">
  <div class="brand"><span class="brand-mark"></span>TARNWELL</div>
  <div class="address">
    <h3>Address</h3>
    <div class="contact-row">
      <svg viewBox="0 0 24 24" fill="#1f3450"><path d="M12 1a8 8 0 0 0-8 8c0 6 8 14 8 14s8-8 8-14a8 8 0 0 0-8-8zm0 11a3 3 0 1 1 0-6 3 3 0 0 1 0 6z"/></svg>
      <span>48 Alder Quay Road,<br>Suite 710 Kingsbridge (QC), Canada<br>K9Z 4T2</span>
    </div>
    <div class="contact-row">
      <svg viewBox="0 0 24 24" fill="#1f3450"><path d="M6 2l4 5-2 3c1 3 3 5 6 6l3-2 5 4-2 4C10 22 2 14 2 4z"/></svg>
      <span>+1 (555) 302-7184</span>
    </div>
    <div class="contact-row">
      <svg viewBox="0 0 24 24" fill="#1f3450"><path d="M2 5h20v2l-10 6L2 7zM2 9l10 6 10-6v10H2z"/></svg>
      <span>hello@tarnwellholdings.com</span>
    </div>
  </div>
</footer>

<div class="bar">
  <span>©Copyrights 2022 Tarnwellcapital</span><span class="sep">|</span><span>All Rights Reserved</span>
  <span class="social" aria-label="Social profile"></span>
</div>
</body>
</html>
```